Helicopter company requires newspaper ad

"Ridgeline Aviation" is an agricultural helicopter company based in Victoria, Australia. We need an advert design for use in newspapers and also possibly social media. Our company specialises in using a helicopter for various agricultural work such as Spraying weeds ("Cropdusting"), spreading fertiliser. This advert will be targeted at farmers in our service area, Our customers are mainly dairy and cow farmers and our services are aimed at increasing their farm productivity. The final design should inform potential and existing customers about our services and the benefits of them. I will attach files of our logo and some existing advertising material for guidance. We would like the ad to feature the blue and green colours in our logo Please feel free to view our website and facebook page to see more about what we do. www.ridgelineaviation.com.au Some text we would like included Spraying: -Accurate -Time Efficient -Zero crop damage -Cost efficient Fertiliser Spreading: -Accurate, Pattern-tested equipment -Zero crop damage or wheel marks -Ability to load product out of a truck, bin or bulk bags -Cost effective, Prices from $32 per hectare depending on spread rate The final advert size should be 195 mm wide x 186 mm high Thanks :)

Farmers, Agriculture Industry

Agribusiness

Designer to choose colors to be used in the design.

• Phone number 0491 736 058
• The text included in the decription, or variations of this

```html
<!DOCTYPE html>
<html lang="en">
<head>
<meta charset="utf-8">
<title>Ridgeline Aviation – Aerial Spraying &amp; Spreading</title>
<link rel="stylesheet" href="https://fonts.googleapis.com/css2?family=Anton&family=Source+Sans+3:ital,wght@0,400;0,700;1,700&display=swap">
<style>
  :root {
    --brand-blue: #2a82fb;
    --brand-navy: #1f3f7a;
    --brand-green: #86f20b;
    --ink: #111111;
    --paper: #ffffff;
    --sky-top: #bfe6f3;
    --sky-low: #e4f2f4;
    --field: #7fae4a;
    --field-dark: #4f7a2c;
  }
  * { box-sizing: border-box; margin: 0; padding: 0; }
  html, body { width: 1200px; height: 1145px; overflow: hidden; background: var(--paper); }
  .advert {
    position: relative;
    width: 1200px;
    height: 1145px;
    font-family: "Source Sans 3", "Myriad Pro", Arial, sans-serif;
    overflow: hidden;
  }
  .header-band {
    position: absolute; left: 0; top: 0; width: 1200px; height: 211px;
    background: var(--brand-blue);
  }
  .brand-box {
    position: absolute; left: 64px; top: 0; width: 376px; height: 263px;
    background: var(--paper);
    display: flex; align-items: center; justify-content: center; gap: 14px;
    z-index: 2;
  }
  .brand-dot {
    width: 30px; height: 30px; border-radius: 50%;
    background: var(--brand-green);
    flex: none;
  }
  .brand-name {
    font-weight: 700; font-size: 40px; line-height: 1.05;
    color: var(--brand-blue);
  }
  .headline {
    position: absolute; left: 490px; top: 30px;
    font-family: "Anton", "Impact", sans-serif;
    font-weight: 400; font-size: 61px; line-height: 64px;
    color: var(--paper);
    text-shadow: 3px 3px 0 var(--brand-navy);
    letter-spacing: 0.5px;
    white-space: nowrap;
  }
  .hero-photo {
    position: absolute; left: 0; top: 211px; width: 1200px; height: 517px;
    background: linear-gradient(180deg, var(--sky-top) 0%, var(--sky-low) 48%, var(--field) 62%, var(--field-dark) 100%);
  }
  .offer-panel {
    position: absolute; left: 0; top: 728px; width: 1200px; height: 307px;
    background: var(--brand-blue);
    color: var(--paper);
  }
  .price-line {
    position: absolute; left: 0; top: 22px; width: 1200px;
    text-align: center;
    font-weight: 700; font-size: 32px; letter-spacing: -0.3px;
  }
  .service-list { position: absolute; top: 88px; }
  .service-list.spraying { left: 68px; }
  .service-list.spreading { left: 593px; }
  .service-title {
    font-weight: 700; font-size: 26px; line-height: 34px;
    margin-left: 45px; margin-bottom: 3px;
  }
  .service-list ul { list-style: none; }
  .service-list li {
    position: relative; padding-left: 45px;
    font-size: 27px; line-height: 39px; font-weight: 400;
  }
  .service-list li::before {
    content: ""; position: absolute; left: 0; top: 10px;
    width: 19px; height: 19px; border-radius: 50%;
    background: var(--paper);
  }
  .contact-footer {
    position: absolute; left: 0; top: 1035px; width: 1200px; height: 110px;
    text-align: center; color: var(--ink);
    font-weight: 700; font-size: 28px; line-height: 40px;
    padding-top: 14px;
  }
  .contact-footer em { font-style: italic; }
</style>
</head>
<body>
<main class="advert">
  <div class="header-band"></div>
  <div class="brand-box">
    <span class="brand-dot"></span>
    <span class="brand-name">Ridgeline<br>Aviation</span>
  </div>
  <h1 class="headline">Do you need your crops<br>Spraying or fertiliser?</h1>

  <div class="hero-photo" role="img" aria-label="Photograph of an agricultural helicopter flying low over green rolling pasture, spraying a fine mist from a wide boom, with a farmhouse and hills behind"></div>

  <section class="offer-panel">
    <p class="price-line">Cost effective, Prices from $32 per hectare depending on spread rate</p>
    <div class="service-list spraying">
      <h2 class="service-title">SPRAYING:</h2>
      <ul>
        <li>Accurate</li>
        <li>Time Efficient</li>
        <li>Zero crop damage</li>
        <li>Cost efficient Fertiliser</li>
      </ul>
    </div>
    <div class="service-list spreading">
      <h2 class="service-title">SPREADING:</h2>
      <ul>
        <li>Accurate, Pattern-tested equipment</li>
        <li>Zero crop damage or wheel marks</li>
        <li>Ability to load product out of a truck,<br>bin or bulk bags</li>
      </ul>
    </div>
  </section>

  <footer class="contact-footer">
    <p>Contact <em>Aerial Agriculture Specialists</em>&nbsp; on:</p>
    <p>Tel: 0491 736 058&nbsp; or email us at www.ridgelineaviation.com.au</p>
  </footer>
</main>
</body>
</html>
```